**** Business card design for LumaSoft ****

For my ICT company LumaSoft I need I need a business card design.

We design, build and host web-applications and we have our own CMS product.

Some good examples are attached.

The information should be:
Joren Velthuis
Managing director
E: j.velthuis@lumasoft-example.nl
M: +31(0)6 57182604
T: +31(0)40 7214589
W: www.lumasoft-example.nl

Address:
Pieter Dommelenlaan 27
5612 KT Eindhoven

Requirements
Must have
• - Use logo (see attachments)
- Double sided
- Distinctive
Nice to have
• - Place for a statement on the back-side: "Designed with knowledge, built with passion"
- HTML code (or Pagecraft)
- Dark (black or dark-gray) side
- Small simple images for telephone, e-mail en Url.
- QR code (only if not disturbing), not required, just an option

```html
<!DOCTYPE html>
<html lang="en">
<head>
<meta charset="utf-8">
<title>LumaSoft business card</title>
<link rel="stylesheet" href="https://fonts.googleapis.com/css2?family=Arimo:wght@400;700&family=Comfortaa:wght@400;700&display=swap">
<style>
  :root {
    --page-bg: #e8e5e0;
    --card-dark: #070b14;
    --card-navy: #122036;
    --glow: #1d3a66;
    --panel-dark: #0f1828;
    --panel-mid: #1b2a40;
    --accent: #3fb2ee;
    --accent-deep: #1f8fd6;
    --sky: #d4eefb;
    --white: #ffffff;
    --ink: #1a1a1a;
    --rule: #c9ced4;
  }
  * { margin: 0; padding: 0; box-sizing: border-box; }
  html, body { width: 1200px; height: 1200px; overflow: hidden; }
  body { background: var(--page-bg); position: relative; font-family: "Arimo", Arial, sans-serif; }

  .card {
    position: absolute;
    left: 212px;
    width: 788px;
    height: 444px;
    border-radius: 10px;
    overflow: hidden;
  }

  /* Front side */
  .card--front {
    top: 102px;
    background:
      radial-gradient(ellipse 60% 75% at 30% 50%, var(--glow) 0%, var(--card-navy) 38%, var(--card-dark) 78%);
  }
  .card--front .circuit-texture {
    position: absolute; inset: 0;
    background: radial-gradient(ellipse 45% 60% at 30% 50%, rgba(63,178,238,0.10), rgba(63,178,238,0) 70%);
  }
  .brand-lockup {
    position: absolute;
    left: 110px; top: 168px;
    display: flex; align-items: center; gap: 40px;
  }
  .brand-dot {
    width: 108px; height: 108px; border-radius: 50%;
    background: var(--accent-deep);
  }
  .brand-name {
    font-family: "Comfortaa", sans-serif;
    font-weight: 700;
    font-size: 84px;
    color: var(--accent);
    letter-spacing: 1px;
  }

  /* Back side */
  .card--back {
    top: 637px;
    background: linear-gradient(180deg, var(--sky) 0%, var(--white) 42%, var(--white) 100%);
  }
  .side-panel {
    position: absolute; left: 0; top: 0; bottom: 0;
    width: 221px;
    background: linear-gradient(180deg, var(--panel-dark) 0%, var(--panel-mid) 100%);
  }
  .holder {
    position: absolute; right: 14px; top: 24px;
    text-align: right; color: var(--white);
  }
  .holder__name { font-weight: 700; font-size: 20px; line-height: 24px; }
  .holder__role { font-size: 18px; line-height: 22px; }

  .statement {
    position: absolute; right: 28px; top: 118px;
    text-align: right;
    font-family: "Comfortaa", sans-serif;
    font-size: 31px; line-height: 46px;
    color: var(--accent);
  }
  .statement strong { font-weight: 700; color: var(--accent-deep); }

  .contact {
    position: absolute; left: 240px; top: 298px;
    font-size: 16px; color: var(--ink);
  }
  .contact__row { display: flex; line-height: 24px; }
  .contact__label { width: 28px; font-weight: 700; }
  .contact__rule { width: 210px; height: 1px; background: var(--rule); margin: 6px 0 4px; }

  .mark {
    position: absolute; left: 610px; top: 300px;
    display: flex; flex-direction: column; align-items: center; gap: 8px;
  }
  .mark__dot { width: 76px; height: 76px; border-radius: 50%; background: var(--accent-deep); }
  .mark__name {
    font-family: "Comfortaa", sans-serif; font-weight: 700;
    font-size: 22px; color: var(--accent-deep);
  }
</style>
</head>
<body>
  <section class="card card--front" aria-label="Card front">
    <div class="circuit-texture" role="img" aria-label="Faint blue circuit texture"></div>
    <div class="brand-lockup">
      <div class="brand-dot"></div>
      <div class="brand-name">LumaSoft</div>
    </div>
  </section>

  <section class="card card--back" aria-label="Card back">
    <div class="side-panel">
      <div class="holder">
        <div class="holder__name">Joren Velthuis</div>
        <div class="holder__role">Managing Director</div>
      </div>
    </div>

    <p class="statement">Designed with <strong>knowledge,</strong><br>built with <strong>passion.</strong></p>

    <div class="contact">
      <div class="contact__row"><span class="contact__label">T</span><span>+31(0)40 7214589</span></div>
      <div class="contact__row"><span class="contact__label">M</span><span>+31(0)6 57182604</span></div>
      <div class="contact__row"><span class="contact__label">E</span><span>j.velthuis@lumasoft-example.nl</span></div>
      <div class="contact__rule"></div>
      <div class="contact__row"><span class="contact__label">A</span><span>Pieter Dommelenlaan 27</span></div>
      <div class="contact__row"><span class="contact__label"></span><span>5612 KT Eindhoven</span></div>
    </div>

    <div class="mark">
      <div class="mark__dot"></div>
      <div class="mark__name">LumaSoft</div>
    </div>
  </section>
</body>
</html>
```